Central Florida Lawn and Landscape business needs an awesome flyer design!

We are a growing lawn and landscape maintenance business looking to incorporate print mail for target advertising. This project should provide some editing capabilities for us to incorporate our logo, update any promotional offers, and adjust throughout the various seasons (lawn service, mulch jobs, one-time clean-ups, hardscape projects, etc). We'd like a clear call to action (one that we can edit if needed) to call or text today. We'll include our website address as well.
The business name is Velo Grassworks.
Target Market(s)
Residential homeowners
Industry/Entity Type
Lawn and landscape maintenance
Font styles to use
Other font styles liked:
- Couture
Look and feel

```html
<!DOCTYPE html>
<html lang="en">
<head>
<meta charset="utf-8">
<title>Velo Grassworks Flyer</title>
<link rel="stylesheet" href="https://fonts.googleapis.com/css2?family=Poppins:wght@400;500;600;700;800&family=Montserrat:wght@700;800;900&display=swap">
<style>
  :root {
    --navy: #262a6e;
    --green: #14964a;
    --green-light: #7cc242;
    --yellow: #f2e81a;
    --dark-green: #1e6b35;
    --white: #ffffff;
    --stage: #e2e2e2;
    --ink: #2b2b45;
  }
  * { margin: 0; padding: 0; box-sizing: border-box; }
  html, body { width: 913px; height: 1200px; overflow: hidden; }
  body { background: var(--stage); font-family: "Poppins", sans-serif; position: relative; }

  .flyer { position: absolute; left: 32px; top: 0; width: 848px; height: 1200px; background: var(--white); overflow: hidden; }

  .hero { position: absolute; left: 0; top: 0; width: 848px; height: 484px; }
  .hero-shapes { position: absolute; left: 0; top: 0; }
  .hero-photo { position: absolute; left: 0; top: 0; width: 560px; height: 484px;
    background: linear-gradient(180deg, #2f5a2a 0%, #4c7a33 30%, #d9d3a0 42%, #8fbf3c 58%, #5ea52c 100%); }

  .brand-badge { position: absolute; left: 23px; top: 20px; width: 216px; height: 216px; border-radius: 50%;
    background: var(--white); border: 13px solid var(--yellow); display: flex; flex-direction: column;
    align-items: center; justify-content: center; text-align: center; }
  .brand-name { font-family: "Poppins", sans-serif; font-weight: 700; font-size: 20px; line-height: 1.1; color: var(--dark-green); }
  .brand-tag { margin-top: 10px; font-size: 9px; line-height: 1.3; color: var(--ink); }

  .headline { position: absolute; left: 26px; top: 292px; font-family: "Montserrat", sans-serif; font-weight: 900;
    font-size: 63px; letter-spacing: 0.5px; color: var(--white); text-shadow: 3px 3px 0 var(--dark-green); }
  .subhead { position: absolute; right: 334px; top: 370px; font-family: "Montserrat", sans-serif; font-weight: 800;
    font-size: 25px; color: var(--white); text-shadow: 2px 2px 0 var(--dark-green); }
  .ribbon-text { position: absolute; left: 31px; top: 421px; font-weight: 600; font-size: 14.5px; color: var(--yellow); }

  .why-title { position: absolute; left: 556px; top: 8px; width: 292px; text-align: center; color: var(--white);
    font-weight: 500; font-size: 28px; }
  .why-list { list-style: none; }
  .why-item { position: absolute; display: flex; align-items: center; gap: 16px; }
  .why-icon { width: 46px; height: 46px; border-radius: 50%; background: var(--white); border: 5px solid var(--yellow);
    display: flex; align-items: center; justify-content: center; flex-shrink: 0; }
  .why-icon svg { display: block; }
  .why-label { font-weight: 500; font-size: 22px; line-height: 1.2; color: var(--yellow); }

  .services-title { position: absolute; left: 0; top: 500px; width: 100%; text-align: center; font-family: "Montserrat", sans-serif;
    font-weight: 800; font-size: 26px; color: var(--navy); }
  .services-intro { position: absolute; left: 0; top: 537px; width: 100%; text-align: center; font-size: 12.5px; color: var(--ink); }

  .service-card { position: absolute; width: 329px; border: 1.5px solid var(--green); border-radius: 10px; background: var(--white); }
  .service-name { position: absolute; left: 50%; top: -17px; transform: translateX(-50%); padding: 0 14px; background: var(--white);
    white-space: nowrap; font-weight: 600; font-size: 23px; line-height: 1.3; color: var(--navy); }
  .service-name .lead { color: var(--green); }
  .service-photo { position: absolute; left: 5px; top: 18px; width: 317px; height: 177px; }
  .service-text { position: absolute; left: 14px; right: 14px; top: 201px; text-align: center; font-size: 10.8px; line-height: 1.3; color: var(--ink); }

  .footer { position: absolute; left: 0; top: 1106px; width: 848px; height: 94px; }
  .footer-shapes { position: absolute; left: 0; top: 0; }
  .contact { position: absolute; display: flex; align-items: center; gap: 7px; color: var(--white); font-weight: 500; font-size: 15.5px; line-height: 1; }
  .contact svg, .phone svg { display: block; flex-shrink: 0; }
  .cta-line { position: absolute; left: 487px; top: 14px; color: var(--white); font-weight: 500; font-size: 14.5px; }
  .cta-line .accent { color: var(--yellow); }
  .phone { position: absolute; left: 513px; top: 40px; display: flex; align-items: center; gap: 8px; color: var(--yellow);
    font-family: "Montserrat", sans-serif; font-weight: 700; font-size: 31px; line-height: 1.2; }
</style>
</head>
<body>
<main class="flyer">

  <section class="hero">
    <div class="hero-photo" role="img" aria-label="Two-storey country house behind a freshly striped green lawn with trees"></div>
    <svg class="hero-shapes" width="848" height="484" viewBox="0 0 848 484" aria-hidden="true">
      <defs>
        <linearGradient id="bandGreen" x1="0" x2="1">
          <stop offset="0" stop-color="#14964a"/><stop offset="1" stop-color="#7cc242"/>
        </linearGradient>
      </defs>
      <polygon points="515,0 578,269 522,484 548,484 604,269 541,0" fill="var(--yellow)"/>
      <polygon points="541,0 604,269 548,484 848,484 848,0" fill="var(--navy)"/>
      <polygon points="541,0 848,0 848,59 555,59" fill="url(#bandGreen)"/>
      <polygon points="0,413 514,413 504,449 0,449" fill="var(--navy)"/>
    </svg>

    <div class="brand-badge">
      <p class="brand-name">VELO<br>GRASSWORKS</p>
      <p class="brand-tag">Central Florida Lawn<br>&amp; Landscape business</p>
    </div>

    <h1 class="headline">TRANSFORM</h1>
    <p class="subhead">YOUR OUTDOOR SPACE!</p>
    <p class="ribbon-text">Let’s make your yard the envy of the neighborhood!</p>

    <h2 class="why-title">Why Choose Us?</h2>
    <ul class="why-list">
      <li class="why-item" style="left:584px;top:88px">
        <span class="why-icon"><svg width="22" height="22" viewBox="0 0 24 24"><circle cx="12" cy="9" r="4" fill="var(--navy)"/><path d="M4 21c0-4.4 3.6-7 8-7s8 2.6 8 7z" fill="var(--navy)"/></svg></span>
        <span class="why-label">Experienced<br>Professionals</span>
      </li>
      <li class="why-item" style="left:608px;top:191px">
        <span class="why-icon"><svg width="22" height="22" viewBox="0 0 24 24"><circle cx="12" cy="12" r="8" fill="none" stroke="var(--navy)" stroke-width="3"/><path d="M8 12l3 3 5-6" fill="none" stroke="var(--navy)" stroke-width="2.2"/></svg></span>
        <span class="why-label">Customized<br>Solutions</span>
      </li>
      <li class="why-item" style="left:608px;top:293px">
        <span class="why-icon"><svg width="22" height="22" viewBox="0 0 24 24"><text x="2" y="19" font-family="Poppins, sans-serif" font-weight="700" font-size="18" fill="var(--navy)">$</text><path d="M14 13l2.5 3 5-7" fill="none" stroke="var(--navy)" stroke-width="2"/></svg></span>
        <span class="why-label">Affordable<br>Rates</span>
      </li>
      <li class="why-item" style="left:584px;top:394px">
        <span class="why-icon"><svg width="22" height="22" viewBox="0 0 24 24"><path d="M3 11h4v10H3zM9 11l4-8c2 0 3 1 2.5 3L15 10h5c1 0 2 1 1.7 2l-2 7.5c-.3 1-1 1.5-2 1.5H9z" fill="none" stroke="var(--navy)" stroke-width="2" stroke-linejoin="round"/></svg></span>
        <span class="why-label">Satisfaction<br>Guaranteed</span>
      </li>
    </ul>
  </section>

  <h2 class="services-title">IS YOUR YARD IN NEED OF A LITTLE TLC?</h2>
  <p class="services-intro">We’ve got you covered! Our expert team specializes in:</p>

  <article class="service-card" style="left:82px;top:585px;height:232px">
    <h3 class="service-name"><span class="lead">Lawn</span> Care</h3>
    <div class="service-photo" role="img" aria-label="Ride-on mower cutting a green lawn" style="background:linear-gradient(180deg,#9aa38a 0%,#c8a442 45%,#5f9f32 70%,#3f7f22 100%)"></div>
    <p class="service-text">Keep your grass lush &amp; healthy with our professional lawn maintenance services.</p>
  </article>

  <article class="service-card" style="left:435px;top:585px;height:232px">
    <h3 class="service-name"><span class="lead">One-Time</span> Clean-Ups</h3>
    <div class="service-photo" role="img" aria-label="Push mower on a sunny backyard lawn" style="background:linear-gradient(180deg,#6f8a4a 0%,#b9b267 35%,#6a6f6a 55%,#5c9a2e 100%)"></div>
    <p class="service-text">Spring cleaning or seasonal tidy-ups, we’ll make your outdoor space shine!</p>
  </article>

  <article class="service-card" style="left:82px;top:849px;height:230px">
    <h3 class="service-name"><span class="lead">Mulch</span> Installation</h3>
    <div class="service-photo" role="img" aria-label="Gloved hands planting seedlings in dark soil" style="background:linear-gradient(160deg,#3a2518 0%,#4a3020 50%,#2f1e14 100%)"></div>
    <p class="service-text">Enhance your garden beds and retain moisture with our high-quality mulch options.</p>
  </article>

  <article class="service-card" style="left:435px;top:849px;height:230px">
    <h3 class="service-name"><span class="lead">Hardscape</span> Projects</h3>
    <div class="service-photo" role="img" aria-label="Curved stamped stone walkway beside a green lawn" style="background:linear-gradient(100deg,#7e7a6f 0%,#a39f92 55%,#4d8a2b 85%,#3c7a22 100%)"></div>
    <p class="service-text">From patios to walkways, we create stunning hardscapes that elevate your landscape.</p>
  </article>

  <footer class="footer">
    <svg class="footer-shapes" width="848" height="94" viewBox="0 0 848 94" aria-hidden="true">
      <defs>
        <linearGradient id="footGreen" x1="0" x2="1">
          <stop offset="0" stop-color="#14964a"/><stop offset="0.7" stop-color="#2ea84a"/><stop offset="1" stop-color="#7cc242"/>
        </linearGradient>
      </defs>
      <polygon points="0,0 470,0 440,94 0,94" fill="url(#footGreen)"/>
      <polygon points="470,0 482,0 452,94 440,94" fill="var(--yellow)"/>
      <polygon points="482,0 848,0 848,94 452,94" fill="var(--navy)"/>
    </svg>
    <p class="contact" style="left:29px;top:17px">
      <svg width="13" height="13" viewBox="0 0 14 14"><circle cx="7" cy="7" r="7" fill="var(--white)"/><path d="M3.5 5h7v4.5h-7zM3.5 5l3.5 2.5L10.5 5" fill="none" stroke="var(--green)" stroke-width="1"/></svg>
      hello@velograssworks.com</p>
    <p class="contact" style="left:278px;top:17px">
      <svg width="13" height="13" viewBox="0 0 14 14"><circle cx="7" cy="7" r="6" fill="none" stroke="var(--white)" stroke-width="1.4"/><path d="M1 7h12M7 1c-3 3-3 9 0 12M7 1c3 3 3 9 0 12" fill="none" stroke="var(--white)" stroke-width="1"/></svg>
      velograssworks.com</p>
    <p class="contact" style="left:29px;top:53px">
      <svg width="13" height="15" viewBox="0 0 14 16"><path d="M7 0a6 6 0 0 1 6 6c0 4.5-6 10-6 10S1 10.5 1 6a6 6 0 0 1 6-6z" fill="var(--white)"/><circle cx="7" cy="6" r="2.2" fill="var(--green)"/></svg>
      Palm Grove, FL, United States</p>
    <p class="cta-line">Contact Us Today for a <span class="accent">Free Estimate!</span></p>
    <p class="phone">
      <svg width="22" height="22" viewBox="0 0 24 24"><circle cx="12" cy="12" r="12" fill="var(--green)"/><path d="M8 6l2.5 0 1 3-1.6 1.2a8 8 0 0 0 3.9 3.9L15 12.5l3 1V16c0 1-1 1.8-2 1.6A10 10 0 0 1 6.4 8C6.2 7 7 6 8 6z" fill="var(--navy)"/></svg>
      813-555-0142</p>
  </footer>

</main>
</body>
</html>
```